Create a Wordpress website and online store for a car performance shop

-Website to be coded in Wordpress AFTER design and be an WooCommerce store (will increase to a proper budget for coding after design has been finalised/picked)

-We are a car performance shop that is offering mechanical services + selling parts online

Industry/Entity Type

Automotive

Logo Text

Brisk Automotive

Number of Pages Required

3 page

Colors
e24097
e667a6
eea4c8
fff9f9

Requirements
Must have
• - Wordpress with WooCommerce store
• - Similar website/store design to what i want - https://kelmarodline.com/default.aspx
• See Website script.docx attached.
• I don't want it to be exact copy but it is a inspiration of what i want my website to look/feel.

```html
<!DOCTYPE html>
<html lang="en">
<head>
<meta charset="utf-8">
<title>Brisk Automotive — Performance Parts &amp; Service</title>
<link href="https://fonts.googleapis.com/css2?family=Roboto:wght@300;400;500;700;900&display=swap" rel="stylesheet">
<style>
:root{
  --pink:#e24097;
  --pink-mid:#e667a6;
  --pink-soft:#eea4c8;
  --blush:#fff9f9;
  --ink:#222;
  --text:#555;
  --muted:#999;
  --line:#e3e3e3;
  --page:#efefef;
  --dark:#1f1f1f;
  --white:#fff;
}
*{box-sizing:border-box;margin:0;padding:0}
html,body{width:1200px;height:2444px;overflow:hidden}
body{font-family:"Roboto",Arial,sans-serif;color:var(--text);background:var(--page);position:relative;font-size:11px}
.abs{position:absolute}
.wrap{left:228px;width:744px}

/* top bar */
.topbar{top:0;left:0;width:1200px;height:28px;background:var(--dark);color:#bbb;font-size:9px;letter-spacing:.5px}
.topbar .l{left:228px;top:9px}
.topbar .r{right:228px;top:9px}
.topbar span{margin-right:14px}
.topbar .r span:last-child{margin-right:0}

/* header */
.header{top:28px;left:0;width:1200px;height:104px;background:var(--white)}
.logo{left:228px;top:22px;color:var(--pink);font-weight:900;font-size:30px;line-height:1;letter-spacing:-.5px}
.logo small{display:block;font-size:10px;font-weight:700;letter-spacing:3px;margin-top:2px}
.hicons{right:300px;top:22px;display:flex;gap:10px;align-items:center}
.hicons .badge{width:22px;height:22px;border-radius:50%;border:1.5px solid var(--pink);display:flex;align-items:center;justify-content:center}
.hcall{right:228px;top:24px;width:62px;font-size:8.5px;color:var(--ink);line-height:1.4}
.hcall b{color:var(--pink)}
.nav{right:228px;top:70px;display:flex;gap:18px;font-size:9.5px;font-weight:700;color:var(--ink);white-space:nowrap}
.nav .on{color:var(--pink)}

/* hero */
.depts{top:180px;left:228px;width:212px;height:400px;background:var(--white);border:1.5px solid var(--pink)}
.depts h3{background:var(--pink);color:var(--white);font-size:10px;font-weight:700;padding:8px 12px;letter-spacing:.5px}
.depts ul{list-style:none;padding:6px 12px}
.depts li{font-size:9px;padding:6.5px 0;border-bottom:1px solid #f0f0f0;color:var(--text)}
.search{top:180px;left:448px;width:524px;height:26px;display:flex;gap:6px}
.search .box{flex:1;background:var(--white);border:1px solid var(--line);display:flex}
.search .box span{flex:1;padding:7px 10px;color:var(--muted);font-size:9px}
.search .box b{background:var(--pink);color:var(--white);font-size:9px;padding:7px 16px}
.search .phone{background:var(--pink);color:var(--white);font-weight:700;font-size:9.5px;padding:7px 14px}
.hero{top:212px;left:448px;width:524px;height:368px;background:var(--white)}
.hero-copy{left:44px;top:80px;width:200px}
.hero h1{font-size:24px;line-height:1.1;color:var(--ink);font-weight:500}
.hero h1 em{font-style:normal;color:var(--pink);font-weight:700;font-size:30px}
.hero p{font-size:9px;line-height:1.5;color:var(--muted);margin:14px 0 20px}
.btn{display:inline-block;background:var(--pink);color:var(--white);font-size:9px;font-weight:700;padding:8px 16px;letter-spacing:.5px}
.hero .art{left:250px;top:50px;width:250px;height:230px;border-radius:50%;background:radial-gradient(circle at 45% 50%,#c9c9c9,#8a8a8a 45%,#d33a3a 62%,#f2f2f2 75%)}

/* features */
.features{top:600px;height:70px;background:var(--white);display:flex}
.feature{flex:1;display:flex;align-items:center;gap:10px;padding-left:22px}
.feature b{display:block;font-size:9px;color:var(--ink)}
.feature span{font-size:8px;color:var(--muted)}
.ficon{width:28px;height:28px;border-radius:50%;background:var(--blush);border:1.5px solid var(--pink);display:flex;align-items:center;justify-content:center}

/* categories */
.sec-title{font-size:17px;color:var(--ink);font-weight:700}
.sec-title::after{content:"";display:block;width:40px;height:2px;background:var(--pink);margin-top:6px}
.cats{top:772px;display:grid;grid-template-columns:repeat(4,1fr);gap:16px 13px}
.cat{background:var(--white);height:176px;position:relative;padding:20px 14px}
.cat .pic{width:70px;height:70px;border-radius:6px;background:linear-gradient(135deg,#d7d7d7,#6f6f6f)}
.cat .info{position:absolute;left:94px;top:20px;right:8px}
.cat h4{font-size:9.5px;color:var(--ink);font-weight:700;margin-bottom:6px}
.cat li{list-style:none;font-size:8px;line-height:1.6;color:var(--muted)}
.cat .more{position:absolute;left:94px;bottom:22px;font-size:8px;color:var(--pink);font-weight:700}

/* interior */
.interior{top:1168px;height:400px;display:flex;gap:8px}
.int-visual{width:212px;background:linear-gradient(160deg,#3a3a3a,#121212);position:relative}
.int-visual h3{position:absolute;left:18px;top:30px;color:var(--white);font-size:21px;font-weight:700;line-height:1.1}
.int-visual h3 span{display:block;color:var(--pink-soft);font-size:17px;font-weight:500}
.int-visual .cta{position:absolute;left:18px;bottom:26px}
.int-body{flex:1;background:var(--white);position:relative}
.tabs{display:flex;gap:24px;padding:14px 18px;border-bottom:1px solid var(--line);font-size:9px;font-weight:700;color:var(--muted)}
.tabs .on{color:var(--ink);border-bottom:2px solid var(--pink);padding-bottom:12px;margin-bottom:-15px}
.arrows{right:14px;top:12px;display:flex;gap:4px}
.arrows i{width:18px;height:18px;border:1px solid var(--line);display:flex;align-items:center;justify-content:center;font-style:normal;font-size:10px;color:var(--muted)}
.products{display:grid;grid-template-columns:repeat(3,1fr);gap:16px;padding:30px 18px}
.prod .pic{height:170px;background:radial-gradient(circle,#555,#bdbdbd 60%,#f4f4f4 72%)}
.prod h5{font-size:9px;font-weight:500;color:var(--ink);margin:16px 0 6px;line-height:1.4}
.stars{color:var(--pink-mid);font-size:9px;letter-spacing:1px}
.prod .row{display:flex;justify-content:space-between;align-items:center;margin-top:8px}
.prod .price{font-size:11px;font-weight:700;color:var(--ink)}
.prod .add{background:var(--dark);color:var(--white);font-size:8px;padding:5px 10px}

/* promos */
.promos{top:1600px;height:100px;display:flex;gap:8px}
.promo{flex:1;position:relative}
.promo.a{background:var(--white);border:2px solid var(--pink)}
.promo.b{background:var(--pink);color:var(--white)}
.promo.a .k{left:20px;top:24px;font-size:9px;color:var(--pink);font-weight:700}
.promo.a h3{left:20px;top:40px;font-size:24px;color:var(--ink);font-weight:900}
.promo.a .pct{left:240px;top:22px;font-size:30px;color:var(--pink);font-weight:900;line-height:1}
.promo.a .pct small{font-size:10px;display:block;color:var(--ink)}
.promo.b .k{left:0;right:0;top:22px;text-align:center;font-size:8.5px;font-weight:700;letter-spacing:1px}
.promo.b h3{left:0;right:0;top:34px;text-align:center;font-size:26px;font-weight:400}
.promo.b .cta{left:0;right:0;top:70px;text-align:center;font-size:8px}

/* testimonial */
.testi{top:1740px;height:280px;background:linear-gradient(90deg,#2a2a2a,#4a4a4a 60%,#2e2e2e)}
.testi .avatar{left:100px;top:92px;width:54px;height:54px;border-radius:50%;background:#8c8c8c;border:3px solid var(--white)}
.testi .quote{left:178px;top:86px;width:360px;color:#ddd;font-size:10px;line-height:1.6}
.testi .name{left:178px;top:150px;color:var(--white);font-size:10px;font-weight:700}
.testi .name span{color:var(--pink-soft);font-weight:400}
.dots{left:0;right:0;top:250px;display:flex;justify-content:center;gap:6px}
.dots i{width:6px;height:6px;border-radius:50%;background:#888}
.dots i.on{background:var(--pink)}

/* footer */
.footer{top:2068px;left:0;width:1200px;height:376px;background:var(--dark)}
.f-logo{left:228px;top:30px;color:var(--pink);font-weight:900;font-size:26px;line-height:1}
.f-logo small{display:block;font-size:9px;letter-spacing:3px;font-weight:700;margin-top:2px}
.f-contact{left:228px;top:84px;color:#aaa;font-size:8.5px;line-height:2}
.f-col{top:36px;color:#aaa;font-size:8.5px}
.f-col h6{color:var(--white);font-size:9.5px;margin-bottom:12px}
.f-col li{list-style:none;line-height:2}
.f-col li::before{content:"› ";color:var(--pink)}
.sub{display:flex;margin:4px 0 18px}
.sub span{width:170px;background:#333;color:#888;padding:7px 8px;font-size:8px}
.sub b{background:var(--pink);width:24px}
.pays{display:flex;gap:5px}
.pays i{width:28px;height:17px;background:#444;border-radius:2px}
.join{left:228px;top:236px;color:var(--white);font-size:9.5px;font-weight:700}
.social{left:228px;top:256px;display:flex;gap:6px}
.social i{width:20px;height:20px;border-radius:50%;background:var(--pink)}
.copyright{left:0;top:340px;width:1200px;height:36px;border-top:1px solid #333;text-align:center;padding-top:13px;color:#888;font-size:8.5px}
</style>
</head>
<body>

<div class="abs topbar">
  <div class="abs l"><span>MY ACCOUNT</span><span>WISHLIST</span><span>CHECKOUT</span></div>
  <div class="abs r"><span>CURRENCY: USD</span><span>ENGLISH</span></div>
</div>

<header class="abs header">
  <div class="abs logo">Brisk<small>AUTOMOTIVE</small></div>
  <div class="abs hicons">
    <span class="badge"><svg width="11" height="11" viewBox="0 0 24 24"><path d="M12 21l-8-8a5 5 0 017-7l1 1 1-1a5 5 0 017 7z" fill="none" stroke="#e24097" stroke-width="2.4"/></svg></span>
    <span class="badge"><svg width="11" height="11" viewBox="0 0 24 24"><path d="M3 4h3l2 11h11l2-8H7" fill="none" stroke="#e24097" stroke-width="2.4"/><circle cx="9" cy="20" r="1.6" fill="#e24097"/><circle cx="18" cy="20" r="1.6" fill="#e24097"/></svg></span>
  </div>
  <div class="abs hcall">MY CART<br><b>$0.00</b></div>
  <nav class="abs nav"><span class="on">HOME</span><span>ABOUT US</span><span>SHOP</span><span>CATEGORIES</span><span>MANUFACTURERS</span><span>BLOG</span><span>CONTACT</span></nav>
</header>

<aside class="abs depts">
  <h3>☰ SHOP DEPARTMENTS</h3>
  <ul>
    <li>Brake Systems</li><li>Engine &amp; Intake Parts</li><li>Exhaust &amp; Turbo Kits</li><li>Suspension Parts</li><li>Car Audio</li><li>Lighting &amp; Electrical</li><li>Interior Accessories</li><li>Wheels &amp; Tyres</li><li>Service Kits</li><li>Oils &amp; Fluids</li><li>Cooling &amp; Radiators</li><li>Tools &amp; Garage</li><li>View All Parts</li>
  </ul>
</aside>

<div class="abs search">
  <div class="box"><span>Search the store by part, brand or category...</span><b>SEARCH</b></div>
  <div class="phone">☎ 555 0148 220</div>
</div>

<section class="abs hero">
  <div class="abs hero-copy">
    <h1>BUY FROM US<br>&amp; GET YOUR<br><em>EXCITING BUNDLE</em></h1>
    <p>Save on brake, suspension and engine upgrades when you bundle parts with a fitting at our shop.</p>
    <span class="btn">SHOP NOW</span>
  </div>
  <div class="abs art" role="img" aria-label="Performance brake disc with red caliper and coil-over shock absorber"></div>
</section>

<section class="abs wrap features">
  <div class="feature"><span class="ficon"><svg width="14" height="14" viewBox="0 0 24 24"><path d="M2 6h12v9H2zM14 9h4l3 3v3h-7z" fill="none" stroke="#e24097" stroke-width="2"/></svg></span><div><b>FREE DELIVERY</b><span>On orders over $99</span></div></div>
  <div class="feature"><span class="ficon"><svg width="14" height="14" viewBox="0 0 24 24"><path d="M4 12a8 8 0 1 0 3-6M4 4v4h4" fill="none" stroke="#e24097" stroke-width="2"/></svg></span><div><b>EASY RETURNS</b><span>30 day return policy</span></div></div>
  <div class="feature"><span class="ficon"><svg width="14" height="14" viewBox="0 0 24 24"><path d="M5 12l5 5 9-10" fill="none" stroke="#e24097" stroke-width="2.4"/></svg></span><div><b>CERTIFIED PARTS</b><span>Quality guaranteed</span></div></div>
  <div class="feature"><span class="ficon"><svg width="14" height="14" viewBox="0 0 24 24"><path d="M5 4h4l2 5-3 2a11 11 0 005 5l2-3 5 2v4a2 2 0 01-2 2A17 17 0 013 6a2 2 0 012-2z" fill="none" stroke="#e24097" stroke-width="2"/></svg></span><div><b>FREE HELP</b><span>Call our mechanics</span></div></div>
</section>

<h2 class="abs sec-title" style="left:228px;top:730px">POPULAR <span style="font-weight:400">CATEGORIES</span></h2>

<section class="abs wrap cats">
  <div class="cat"><div class="pic" role="img" aria-label="Car body parts"></div><div class="info"><h4>BODY PARTS</h4><ul><li>Bumpers</li><li>Mirrors</li><li>Fenders</li><li>Bonnets</li></ul></div><span class="more">Browse All ›</span></div>
  <div class="cat"><div class="pic" role="img" aria-label="Car electronics"></div><div class="info"><h4>ELECTRONICS</h4><ul><li>Gauges</li><li>Ignition Parts</li><li>Sensors</li><li>Batteries</li></ul></div><span class="more">Browse All ›</span></div>
  <div class="cat"><div class="pic" role="img" aria-label="Headlight units"></div><div class="info"><h4>LIGHTING</h4><ul><li>Headlights</li><li>Tail Lights</li><li>LED Bulbs</li><li>Fog Lights</li></ul></div><span class="more">Browse All ›</span></div>
  <div class="cat"><div class="pic" role="img" aria-label="Engine performance parts"></div><div class="info"><h4>PERFORMANCE PARTS</h4><ul><li>Air Intakes</li><li>Turbo Kits</li><li>Exhausts</li><li>Intercoolers</li></ul></div><span class="more">Browse All ›</span></div>
  <div class="cat"><div class="pic" role="img" aria-label="Brake and repair parts"></div><div class="info"><h4>REPAIR PARTS</h4><ul><li>Brake Pads</li><li>Filters</li><li>Belts</li><li>Clutches</li></ul></div><span class="more">Browse All ›</span></div>
  <div class="cat"><div class="pic" role="img" aria-label="Wheel rims"></div><div class="info"><h4>WHEELS AND TIRES</h4><ul><li>Alloy Wheels</li><li>Tyres</li><li>Wheel Nuts</li><li>Spacers</li></ul></div><span class="more">Browse All ›</span></div>
  <div class="cat"><div class="pic" role="img" aria-label="Suspension shock absorbers"></div><div class="info"><h4>SUSPENSION</h4><ul><li>Coilovers</li><li>Springs</li><li>Sway Bars</li><li>Bushings</li></ul></div><span class="more">Browse All ›</span></div>
  <div class="cat"><div class="pic" role="img" aria-label="Car care products"></div><div class="info"><h4>CAR CARE</h4><ul><li>Oils</li><li>Polish</li><li>Cleaners</li><li>Coolant</li></ul></div><span class="more">Browse All ›</span></div>
</section>

<section class="abs wrap interior">
  <div class="int-visual" role="img" aria-label="Dark car interior with speakers">
    <h3>INTERIOR<span>&amp; ACCESSORIES</span></h3>
    <span class="btn cta">SHOP NOW</span>
  </div>
  <div class="int-body">
    <div class="tabs"><span class="on">CAR AUDIO</span><span>SEATING</span><span>STEERING WHEELS</span></div>
    <div class="abs arrows"><i>‹</i><i>›</i></div>
    <div class="products">
      <div class="prod"><div class="pic" role="img" aria-label="Pair of coaxial car speakers"></div><h5>Sonexa Sport Coaxial Speaker Pair, 6.5 Inch</h5><div class="stars">★★★★★</div><div class="row"><span class="price">$ 80.00</span><span class="add">ADD TO CART</span></div></div>
      <div class="prod"><div class="pic" role="img" aria-label="Turbocharger unit"></div><h5>Vortane Turbo Charger Kit, Twin Scroll Unit</h5><div class="stars">★★★★★</div><div class="row"><span class="price">$ 80.00</span><span class="add">ADD TO CART</span></div></div>
      <div class="prod"><div class="pic" role="img" aria-label="Car alternator"></div><h5>Corvane High Output Alternator, 150 Amp</h5><div class="stars">★★★★★</div><div class="row"><span class="price">$ 80.00</span><span class="add">ADD TO CART</span></div></div>
    </div>
  </div>
</section>

<section class="abs wrap promos">
  <div class="promo a">
    <span class="abs k">SEASONAL CLEARANCE</span>
    <h3 class="abs">HURRY UP!</h3>
    <div class="abs pct">75<span style="font-size:16px">%</span><small>OFF SELECTED</small></div>
  </div>
  <div class="promo b">
    <span class="abs k">ORIGINAL CAR PARTS</span>
    <h3 class="abs">discover new arrivals</h3>
    <span class="abs cta">SHOP NOW ›</span>
  </div>
</section>

<section class="abs wrap testi" role="img" aria-label="Dark car dashboard backdrop">
  <div class="abs avatar" role="img" aria-label="Customer portrait"></div>
  <p class="abs quote">“Brisk fitted my new coilovers and brakes in a single day and the car has never felt better. Fair prices, real advice, and parts that actually arrive when they say.”</p>
  <div class="abs name">JAMES HOLT <span>— Track Day Driver</span></div>
  <div class="abs dots"><i></i><i class="on"></i><i></i><i></i></div>
</section>

<footer class="abs footer">
  <div class="abs f-logo">Brisk<small>AUTOMOTIVE</small></div>
  <div class="abs f-contact">⌖ 24 Forge Lane, Halden Park<br>☎ +1 555 0148 220<br>✉ hello@briskautomotive.com</div>
  <div class="abs f-col" style="left:440px"><h6>INFORMATION</h6><ul><li>About Us</li><li>Delivery Info</li><li>Privacy Policy</li><li>Terms &amp; Conditions</li><li>Contact Us</li></ul></div>
  <div class="abs f-col" style="left:560px"><h6>WHY BUY FROM US</h6><ul><li>Shipping</li><li>Secure Payment</li><li>Returns</li><li>Warranty</li><li>Workshop Service</li><li>Gift Vouchers</li><li>Help Centre</li><li>Track Order</li></ul></div>
  <div class="abs f-col" style="left:740px"><h6>SUBSCRIBE AND GET 10% DISCOUNT</h6>
    <div class="sub"><span>Enter your email address</span><b></b></div>
    <h6>WE ACCEPT</h6>
    <div class="pays"><i></i><i></i><i></i><i></i><i></i></div>
  </div>
  <div class="abs join">JOIN US</div>
  <div class="abs social"><i></i><i></i><i></i><i></i></div>
  <div class="abs copyright">Copyright © 2024 Brisk Automotive. All rights reserved.</div>
</footer>

</body>
</html>
```